Prominent Trial Lawyer need a Brochure Design for his firm

Douglas R. Pembry of The Pembry Law Firm has been successfully trying severe and complex for over 28 years. He holds the largest verdict in the history of South Georgia of $84,000,000.00 before the late Gerald T. Voskin in the Harlow District of the Lower District of Marren. He specializes in sever injuries, whether by auto accident, trucking accident or medical malpractice. He is also well know for his successful trial of business disputes and high net-worth Divorces.
Target Market(s)
Persons who need an aggressive, experienced trial lawyer especially for personal injury, but also for other civil and business matters, high end divorde
Industry/Entity Type
Medical
Contact Information for Business Card
Need to use coloring and logo uplaoded
Requirements
Must have
- 1) biography of principal, Douglas R. Pembry
- 2) what we do
- 3) specific cases handled, with specific outcomes (will be supplied)

```html
<!DOCTYPE html>
<html lang="en">
<head>
<meta charset="utf-8">
<title>The Pembry Law Firm — Brochure and Business Card</title>
<link rel="stylesheet" href="https://fonts.googleapis.com/css2?family=Crimson+Pro:wght@400;600&family=Arimo:wght@400;700&display=swap">
<style>
:root{
  --red:#e8202a;
  --dark:#221f20;
  --ink:#1c1c1c;
  --paper:#ffffff;
  --bg:#ebebeb;
  --serif:"Crimson Pro", Georgia, serif;
  --sans:"Arimo", Arial, sans-serif;
}
*{margin:0;padding:0;box-sizing:border-box}
html,body{width:1200px;height:1000px;overflow:hidden;background:var(--bg)}
.canvas{position:relative;width:1200px;height:1000px;font-family:var(--sans);color:var(--ink)}
.abs{position:absolute}

/* ---------- brochure outside ---------- */
.outside{left:40px;top:80px;width:527px;height:410px;background:var(--dark);overflow:hidden}
.team-photo{left:0;top:0;width:175px;height:225px;background:linear-gradient(160deg,#5b534c 0%,#2f2b2a 55%,#1d1b1c 100%)}
.gavel-photo{left:175px;top:0;width:352px;height:225px;background:linear-gradient(120deg,#9eb0e0 0%,#7a86b6 35%,#6a4a36 70%,#2a1a12 100%)}
.motto{left:196px;top:42px;width:150px;color:#fff;font-family:var(--serif)}
.motto h2{font-size:18px;font-weight:600;letter-spacing:1px;margin-bottom:8px}
.motto blockquote{font-size:14.5px;line-height:1.15;text-align:center}
.motto cite{display:block;font-style:normal;font-size:12px;margin-top:10px;text-align:center}
.firm-band{left:0;top:225px;width:175px;height:25px;background:var(--red);color:#fff;font-family:var(--serif);font-size:14px;font-weight:600;text-align:center;line-height:25px;letter-spacing:1px}
.firm-text{left:10px;top:258px;width:156px;color:#fff;font-size:6.4px;line-height:1.5;text-align:center}
.logo-band{left:175px;top:225px;width:352px;height:73px;background:var(--paper);border-bottom:5px solid var(--red)}
.logo{display:flex;align-items:center;gap:6px;position:absolute;font-family:var(--serif);font-weight:600;color:var(--ink)}
.logo .mark{border-radius:50%;background:var(--red);flex:none}
.logo span{line-height:1}
.logo-band .logo{top:18px;font-size:15px}
.logo-band .logo .mark{width:32px;height:32px}
.office{left:175px;top:310px;width:175px;color:#fff;text-align:center}
.office h3{font-family:var(--serif);font-size:14px;font-weight:600;margin-bottom:3px}
.office p{font-size:10px;line-height:1.3}
.office .web{font-family:var(--serif);font-size:15px;font-weight:600;margin-top:6px}
.gavel-lower{left:350px;top:303px;width:177px;height:107px;background:linear-gradient(160deg,#3a2418 0%,#7b4a2c 45%,#241510 100%)}

/* ---------- business card ---------- */
.card{left:627px;top:126px;width:543px;height:317px;background:var(--paper)}
.card .logo{left:28px;top:118px;font-size:21px}
.card .logo .mark{width:44px;height:44px}
.card-panel{left:253px;top:21px;width:271px;height:278px;background:var(--red);color:#fff;padding:24px 14px}
.card-panel h2{font-family:var(--serif);font-size:19px;font-weight:600;letter-spacing:.5px}
.card-panel .role{font-size:13px;margin-bottom:22px}
.contact{list-style:none;font-size:13.5px}
.contact li{display:flex;align-items:center;gap:10px;height:21px}
.contact svg{width:11px;height:11px;flex:none}
.contact .gap{height:22px}

/* ---------- brochure inside ---------- */
.inside{left:333px;top:515px;width:528px;height:408px;background:var(--paper);overflow:hidden}
.practice-head{left:0;top:0;width:352px;height:45px;background:var(--dark);color:#fff;font-family:var(--serif);font-size:26px;font-weight:600;letter-spacing:1.5px;padding-left:15px;line-height:45px}
.area-bar{height:30px;background:var(--red);color:#fff;font-family:var(--serif);font-size:15.5px;font-weight:600;padding-left:15px;line-height:30px}
.area-text{font-size:5.4px;line-height:1.55;color:#333;padding:0 12px 0 15px;overflow:hidden}
.area-text p{margin-bottom:5px}
.area-text b{color:var(--ink)}
.bio-col{left:352px;top:0;width:176px;height:408px;background:var(--dark)}
.bio-name{height:43px;background:var(--red);color:#fff;font-family:var(--serif);font-size:16px;font-weight:600;padding-left:12px;line-height:50px}
.portrait{height:150px;background:linear-gradient(170deg,#5d6370 0%,#3a3d47 50%,#1e2027 100%)}
.bio-text{color:#fff;font-size:6.8px;line-height:1.5;padding:8px 12px 0}
.contact-us{left:0;top:318px;width:176px;height:90px;background:var(--red);color:#fff;padding:6px 13px;font-family:var(--serif)}
.contact-us h3{font-size:20px;font-weight:600;letter-spacing:1px;line-height:1.1}
.contact-us .phone{display:flex;align-items:center;gap:8px;font-size:18px;font-weight:600;border-bottom:1.5px solid #fff;padding-bottom:2px}
.contact-us .phone svg{width:13px;height:13px}
.contact-us .web{font-size:18px;margin-top:2px}
</style>
</head>
<body>
<div class="canvas">

  <section class="abs outside">
    <div class="abs team-photo" role="img" aria-label="Photo of the firm's three attorneys posed in business attire"></div>
    <div class="abs gavel-photo" role="img" aria-label="Close-up photo of a wooden judge's gavel"></div>
    <div class="abs motto">
      <h2>OUR MOTTO</h2>
      <blockquote>“Whether you are against Insurance Companies, Fortune 500 Companies or Goverments, we level the field and give you the edge.”</blockquote>
      <cite>- The Pembry Law Firm</cite>
    </div>
    <h2 class="abs firm-band">OUR FIRM</h2>
    <p class="abs firm-text">Founded in 1989, the firm practices in business and general civil litigation, personal injury, real estate transaction and litigation, criminal defense, and family law. We love the practice of law and how it can help to resolve your civil and family disputes, to right the wrongs done by others, to protect your constitutional rights if you happened to be accused of a crime, to seek fair monetary compensation if you are entitled to. We at The Pembry Law Firm can ensure that you are best represented in courts utilizing the most up-to-date laws, diligent preparation and insightful understanding of your matter.</p>
    <div class="abs logo-band">
      <div class="logo" style="left:14px"><i class="mark"></i><span>The Pembry<br>Law Firm</span></div>
      <div class="logo" style="left:188px"><i class="mark"></i><span>The Pembry<br>Law Firm</span></div>
    </div>
    <div class="abs office">
      <h3>Our Office:</h3>
      <p>14 Orrin Way, Calder, GA 30000<br>555 - 018 - 2290<br>dpembry@drplaw.com</p>
      <p class="web">www.drplaw.com</p>
    </div>
    <div class="abs gavel-lower" role="img" aria-label="Photo detail of a wooden gavel handle"></div>
  </section>

  <section class="abs card">
    <div class="logo"><i class="mark"></i><span>The Pembry<br>Law Firm</span></div>
    <div class="abs card-panel">
      <h2>DOUGLAS PEMBRY</h2>
      <p class="role">LAWYER</p>
      <ul class="contact">
        <li><svg viewBox="0 0 12 12"><path d="M3 1h2l1 3-1.5 1a6 6 0 0 0 2.5 2.5L8 6l3 1v2c0 1-1 2-2 2A8 8 0 0 1 1 3c0-1 1-2 2-2z" fill="#fff"/></svg>555 - 018 - 2290</li>
        <li><svg viewBox="0 0 12 12"><rect x="0.5" y="2" width="11" height="8" fill="#fff"/><path d="M0.5 2l5.5 4.5L11.5 2" stroke="#e8202a" fill="none"/></svg>dpembry@drplaw.com</li>
        <li class="gap"></li>
        <li><svg viewBox="0 0 12 12"><path d="M6 0.5a4 4 0 0 1 4 4c0 3-4 7-4 7s-4-4-4-7a4 4 0 0 1 4-4z" fill="#fff"/><circle cx="6" cy="4.5" r="1.5" fill="#e8202a"/></svg>14 Orrin Way, Calder, GA 30000</li>
        <li><svg viewBox="0 0 12 12"><path d="M3 1h2l1 3-1.5 1a6 6 0 0 0 2.5 2.5L8 6l3 1v2c0 1-1 2-2 2A8 8 0 0 1 1 3c0-1 1-2 2-2z" fill="#fff"/></svg>555 - 018 - 2290</li>
        <li><svg viewBox="0 0 12 12"><rect x="0.5" y="2" width="11" height="8" fill="#fff"/><path d="M0.5 2l5.5 4.5L11.5 2" stroke="#e8202a" fill="none"/></svg>dpembry@drplaw.com</li>
        <li class="gap"></li>
        <li><svg viewBox="0 0 12 12"><circle cx="6" cy="6" r="5" fill="none" stroke="#fff"/><ellipse cx="6" cy="6" rx="2.2" ry="5" fill="none" stroke="#fff"/><path d="M1 6h10" stroke="#fff"/></svg>www.drplaw.com</li>
      </ul>
    </div>
  </section>

  <section class="abs inside">
    <h1 class="abs practice-head">OUR PRACTICE AREA</h1>

    <div class="abs" style="left:0;top:45px;width:176px">
      <h2 class="area-bar">Personal Injury</h2>
      <div class="area-text" style="height:90px;padding-top:8px">
        <p>If you or loved ones get injured because of negligence of another, you may be entitled to compensation for your pain and suffering and loss of earnings. We handle injuries caused by automobile accidents, slip and fall, medical malpractice, dog bites and other accidents. We take injury cases on a contingency basis and you do not pay attorneys' fees in advance. We can also help you secure medical care if you cannot afford it. Contact us for a free evaluation.</p>
      </div>
      <h2 class="area-bar">Criminal Defense</h2>
      <div class="area-text" style="padding-top:8px">
        <p>The Pembry Law Firm handles various criminal matters including but not limited to DUI, Assault and Battery, Theft, Forgery, Traffic Violations, Domestic Violence and Drug cases. We will do our utmost to achieve the best possible results. We will represent you for a jury trial as well to prove your innocence of the crime you are accused of. We promise to keep confidentiality when handling your sensitive criminal case and help you throughout this extremely stressful experience.</p>
        <p>If you, or a friend or family member, have been charged with a crime, an uncertain future lies ahead. It is important to have an attorney who knows what to expect in a criminal case, to explain the process, and to help make informed decisions about the best course of action. Our attorneys have represented clients who face all types of criminal charges, including:</p>
        <p><b>DUI; Drug-related offenses; Criminal Internet Offenses; Traffic violations; White collar crime; Felonies and Misdemeanors</b></p>
        <p>Our attorneys have extensive experience in trying criminal cases. We will not take any case we are not prepared to take to trial.</p>
      </div>
    </div>

    <div class="abs" style="left:176px;top:45px;width:176px">
      <h2 class="area-bar">Business Law</h2>
      <div class="area-text" style="height:140px;padding-top:8px">
        <p>The structure of your business enterprise is important. Should you form a corporation, an LLC or a general or limited partnership? We can explain the differences and help you make a choice.</p>
        <p>Once you've decided, we can form that entity and have you up and running in a matter of days with a tax payer identification number ready to do business.</p>
        <p>The term “business” has as many different meanings as there are people on the planet. Sometimes it is a matter of someone lending another person money. We can draft that promissory note. Sometimes it is an employment agreement, a non-competition agreement, or a franchise agreement. We have extensive experience in all these areas as well as commercial and private real estate.</p>
      </div>
      <h2 class="area-bar">Civil Litigation</h2>
      <div class="area-text" style="padding-top:8px">
        <p>The term civil litigation encompasses wide array of civil actions. The firm can handle various assignments including but not limited to:</p>
        <p><b>Breach of contract; Real Estate Transaction/Litigation; Administrative Hearings for licenses; Name Changes; Insurance Bad Faith; Fraud; Sale and Purchase of Businesses; and, Probate and Estate Planning</b></p>
        <p>Our office has a dynamic litigation practice with years of experience in State and Federal Courts. Our attorneys have tried many cases to jury verdict in a broad range of subjects including real estate, business, personal injury, and wrongful death. We employ state of the art technological tools and extensive research capabilities. Our litigation philosophy is not to take any case we are not prepared to take to a jury.</p>
      </div>
    </div>

    <aside class="abs bio-col">
      <h2 class="bio-name">Douglas Pembry</h2>
      <div class="portrait" role="img" aria-label="Portrait photo of Douglas R. Pembry in a suit and red tie"></div>
      <p class="bio-text">Douglas graduated with honors from the Marren State School of Law in 1993. He also received his BBA from Marren State in 1989. Douglas has spent the last 22 years trying complex cases, including medical malpractice, personal injury, criminal and civil cases. He holds the largest verdict in the Lower District of Marren of $84,000,000.00. Currently he specializes in severe personal injury cases and commercial litigation.</p>
      <div class="abs contact-us">
        <h3>CONTACT US</h3>
        <p class="phone"><svg viewBox="0 0 12 12"><path d="M3 1h2l1 3-1.5 1a6 6 0 0 0 2.5 2.5L8 6l3 1v2c0 1-1 2-2 2A8 8 0 0 1 1 3c0-1 1-2 2-2z" fill="#fff"/></svg>555.014.7720</p>
        <p class="web">www.drplaw.com</p>
      </div>
    </aside>
  </section>

</div>
</body>
</html>
```